Marketing / Informational Site for Marriage and Family Therapists Cooperative

We need a web design for a new Marriage and Family Therapist Cooperative, called Meadowgate Counselors. This is a market and information site for potential clients and referrals to learn more about the team and get contact information.

We are looking for profession, clean, and modern design, that cater towards families and mom's concerned about their families mental health and child development.

This should include a home page, an general about page, 3 bio pages (1 for each therapist listed below), and a general contact us page.

Our Domain Name

Meadowgatecounselors.example

Company Name

Meadowgate Counselors

Group Moto/Philosophy

“Our sorrows and wounds are healed only when we touch them with compassion.” - Orvelan

Our Logo

See Heron Final (attached)

Home Page (Introduction)

Feeling stressed and overwhelmed?
Encountering barriers towards your goals?
Having difficulty accomplishing the simplest task?
Have the need to talk but unsure who to turn to?

Therapy can assist you in overcoming all of these challenges. Assist you in uncovering the difficulties and barriers that are keeping you from achieving your life’s ambitions, help discover ways to overcome them, and cope with the impact your behaviour has on your occupation, personal life and social life.

Welcome to our practice, with over 20 years of combined experience in the clinical field you are sure to find the right fit for your needs. Each clinician has experience working with groups, adults, teens, children, families, and couples. We specialize in fostering healthy relationships between individuals, managing depression and anxiety, overcoming trauma, and developing occupational success. Feel free to explore information about each clinician and make an appointment with one of us today.

About Us (bio pics attached)

Marisel Dunkworth

My name is Dr. MariSel Dunkworth and I am a Licensed Marriage Family Therapist with a practice in Riverside, CA. I have devoted my life’s work into developing my skills in this profession. I have over 15 years of experience working in the clinical and the social service settings. These years have afforded me the opportunity to work with groups, families, adults, teens and children with varying symptoms. I have helped clients that have trauma, abuse histories, and many within the legal or social service systems. I enjoy working individuals from all walks of life achieve self sufficiency, social success and occupational success. In my years of training I have come to develop a culturally sensitive practice that centers around the needs of the client.

I have held many positions in my clinical career beginning as clinician moving upwards toward supervisor and program coordinator. I have also over 5 years of experience as an adjunct faculty member in the University setting teaching student to become Marriage and Family Therapists. As a clinician I focused on enriching my clinical skills by developing outcome driven practices to achieve client’s desired goals. As a clinical supervisor, I guided clinicians along their own paths towards clinical licensure. As a program coordinator, I helped develop a clinical assessment and triage program from ground up to assist client in accessing services in the South Los Angeles Area. The program would assist over 100 plus clients on a monthly basis get connected to clinical services and linked to any additional resources as needed by the individual. I have graduated with my, Bachelor’s degree at the Halvern College, Riverside. I received my Masters degree in Clinical Psychology at Mount St. Mary’s University, and my Doctorate degree in Clinical Psychology at Tamsworth Institute.

To schedule an appointment with Dr. MariSel Dunkworth, LMFT:

email: marisel582@postbox.example
Phone: (951)555-0182

Jeb Kowal

My name is Rosalindra (Jeb) Kowal, I received my Masters Degree of Counseling in Marriage and Family Therapy from Corvell Bay State College in June 2000. I have acquired over 15 years of experience helping Individuals, Couples, and Families cope with issues of Anxiety, Depression, Grief and Bereavement, and HIV/AIDS.

I am a Family Systems Therapist and I truly believe the dynamics in our family of origin greatly shape our current belief systems and behaviors. However, I often utilize a variety of approaches to help my clients achieve their goals depending on their individual needs.

My greatest strength as a Marriage and Family Therapist is helping my clients explore ways to make the changes in their lives that will allow them to live their life to their fullest potential. I help my clients achieve their personal life goals with a warm, safe, non-judgmental , and supportive environment. In doing so, my clients are encouraged to explore the issues that may be preventing them from living the life they desire. Thus, empowering them to take control of their personal journey to living a productive and meaningful life.

If you feel that you are ready to commit to bringing about positive changes in your life and would like support in exploring this path, I’m here to work with you in your journey to personal growth and development.

To schedule an appointment with Rosalindra Kowal, LMFT:

e-mail: rkjeb7@mailnest.example
Phone: (951)555-0147

Dena Holcroft

Dena Holcroft graduated with a Masters in Marriage and Family Therapy from Pellridge Crestwood College. She currently holds a license in Marriage and Family Therapy in the State of California. She is also formally trained in Clinical Art Therapy. Dena's expertise lies in providing treatment to individuals experiencing work-related injuries, severe physical and emotional pain, trauma, grief and loss, anxiety and depression. In her early career, she provided valuable service at the largest free clinic in the nation serving marginalized families and children. For the past ten years, Dena has worked with HIV/AIDS population.
Dena comes from a multicultural background and she has utilized this experience and knowledge in serving a variety of populations. At an organizational level, Dena has worked extensively with challenging issues such as the chemical dependency and homelessness. In her private practice, Dena is proficient in working within individuals experiencing relationship concerns, marital and family conflict, depression/anxiety, self-esteem concerns, adjustment disorders, and pain management. She has treated clients from diverse cultural, linguistic backgrounds and sexual orientations.
Dena is trained in Family Systems Theory and incorporates other strategies appropriate for each presenting issue. She specializes in Clinical Art Therapy and has successfully utilized an integrated approach including guided imagery and relaxation skills training for many years.

To schedule an appointment with Dena Holcroft, LMFT

e-mail: greypinestudio@inkmail.example
Phone: (951) 555-0169

Target Market(s)

Families with child development, marriage issues, or other mental health needs

Industry/Entity Type

Marketing

Number of Pages Required

5+ page

Requirements
Must have
• 1 home page, 1 about page, 1 contact page. About page could either be standalone page with 3 different bio pages for each therapist or an all in one about page that includes bios for all 3 therapists.

```html
<!DOCTYPE html>
<html lang="en">
<head>
<meta charset="utf-8">
<title>Meadowgate Counselors — Marriage and Family Therapist Cooperative</title>
<link rel="stylesheet" href="https://fonts.googleapis.com/css2?family=Open+Sans:wght@400;600;700&family=Roboto+Condensed:wght@400;700&display=swap">
<style>
:root{
  --green:#a9c23f;
  --green-dark:#8fa82c;
  --ink:#333333;
  --muted:#777777;
  --light:#f1f1f1;
  --line:#e2e2e2;
  --footer:#1f1f1f;
  --footer-deep:#151515;
  --white:#ffffff;
}
*{box-sizing:border-box;margin:0;padding:0}
html,body{width:1200px;height:2168px;overflow:hidden}
body{font-family:"Open Sans",Arial,sans-serif;color:var(--ink);background:var(--white);position:relative}
a{color:inherit;text-decoration:none}

/* header */
.site-header{position:absolute;top:0;left:0;width:1200px;height:144px;background:var(--white)}
.brand{position:absolute;left:90px;top:40px;display:flex;align-items:center;gap:12px}
.brand-mark{width:22px;height:22px;background:var(--green);border-radius:50%}
.brand-name{font-family:"Open Sans",sans-serif;font-weight:600;font-size:20px;color:var(--ink)}
.utility{position:absolute;right:90px;top:22px;display:flex;gap:26px;font-size:13px;color:var(--muted)}
.utility span{display:flex;align-items:center;gap:6px}
.main-nav{position:absolute;right:60px;top:88px;display:flex}
.main-nav a{font-size:15px;font-weight:600;letter-spacing:.5px;color:var(--ink);padding:8px 34px;border-left:1px solid var(--line)}
.main-nav a:first-child{border-left:none}
.main-nav a.active{color:var(--green);border-bottom:3px solid var(--green)}

/* hero */
.hero{position:absolute;top:144px;left:0;width:1200px;height:656px;overflow:hidden}
.hero-photo{position:absolute;inset:0;background:linear-gradient(100deg,#3a3430 0%,#6e6863 30%,#9aa4ac 60%,#c8ccd0 100%)}
.hero-quote{position:absolute;right:90px;top:96px;text-align:right;font-family:"Roboto Condensed",sans-serif;font-weight:700;font-size:50px;line-height:60px;color:var(--white);text-transform:uppercase}
.hero-quote .accent{color:var(--green)}
.hero-quote .author{display:block;font-size:34px;line-height:52px}
.hero-arrows{position:absolute;right:90px;bottom:36px;display:flex;gap:6px}
.hero-arrows span{width:32px;height:32px;background:rgba(0,0,0,.55);display:flex;align-items:center;justify-content:center}

/* intro */
.intro{position:absolute;top:850px;left:100px;width:1000px;height:340px}
.intro-copy{position:absolute;left:0;top:0;width:700px}
.intro-copy h1{font-family:"Open Sans",sans-serif;font-weight:600;font-size:26px;color:var(--ink);margin-bottom:22px;letter-spacing:.3px}
.intro-copy p{font-size:12.5px;line-height:20px;color:var(--muted);margin-bottom:14px}
.btn{display:inline-block;background:var(--green);color:var(--white);font-weight:700;font-size:12px;padding:11px 22px;letter-spacing:.5px}
.contact-box{position:absolute;right:0;top:0;width:260px;height:310px;background:#f4f7e6;border:1px solid #dfe7bd}
.contact-box header{background:var(--green);color:var(--white);text-align:center;padding:14px 0 16px}
.contact-box header .label{font-size:18px}
.contact-box header .phone{font-size:24px;font-weight:700}
.contact-box form{padding:16px 20px}
.field{height:30px;background:var(--white);border:1px solid var(--line);margin-bottom:10px}
.field.tall{height:56px}
.contact-box .btn{padding:8px 20px;font-size:11px}

/* features */
.features{position:absolute;top:1240px;left:0;width:1200px;height:430px;background:var(--light)}
.feature{position:absolute;top:30px;width:320px}
.feature-photo{width:320px;height:190px}
.feature h2{font-size:15px;font-weight:700;color:var(--ink);margin:22px 0 10px}
.feature p{font-size:12.5px;line-height:20px;color:var(--muted)}

/* testimonial */
.testimonial{position:absolute;top:1680px;left:100px;width:1000px;height:220px}
.testimonial-photo{position:absolute;left:0;top:0;width:180px;height:190px}
.quote-mark{position:absolute;font-family:Georgia,serif;font-size:70px;color:#cfcfcf;line-height:1}
.testimonial blockquote{position:absolute;left:250px;top:20px;width:700px;font-size:13px;line-height:21px;color:var(--muted)}
.testimonial blockquote .hl{color:var(--green)}
.testimonial cite{position:absolute;right:30px;top:128px;font-style:normal;font-size:14px;color:var(--ink)}
.dots{position:absolute;left:460px;top:170px;display:flex;gap:10px}
.dots span{width:9px;height:9px;border-radius:50%;background:#c9c9c9}
.dots span.on{background:var(--ink)}

/* footer */
.site-footer{position:absolute;top:1920px;left:0;width:1200px;height:248px;background:var(--footer);color:#bdbdbd}
.footer-col{position:absolute;top:34px}
.footer-col h3{font-size:14px;font-weight:700;color:var(--white);margin-bottom:16px}
.footer-col li{list-style:none;font-size:12px;line-height:22px}
.footer-col p{font-size:12px;line-height:18px}
.news-row{display:flex;margin-top:14px}
.news-row .input{width:200px;height:32px;background:var(--white)}
.news-row .go{height:32px;background:var(--green);color:var(--white);font-size:11px;font-weight:700;padding:9px 14px}
.contact-list li{display:flex;gap:8px;align-items:flex-start}
.contact-list svg{flex:none;margin-top:5px}
.copyright{position:absolute;bottom:0;left:0;width:1200px;height:36px;background:var(--footer-deep);text-align:center;font-size:11px;line-height:36px;color:#8a8a8a}
</style>
</head>
<body>

<header class="site-header">
  <a class="brand" href="#"><span class="brand-mark"></span><span class="brand-name">Meadowgate Counselors</span></a>
  <div class="utility">
    <span><svg width="11" height="11" viewBox="0 0 11 11"><circle cx="5.5" cy="3.5" r="2.5" fill="#999"/><path d="M1 11c0-3 2-4.5 4.5-4.5S10 8 10 11z" fill="#999"/></svg>Sign in</span>
    <span>Follow:
      <svg width="40" height="10" viewBox="0 0 40 10"><circle cx="5" cy="5" r="4" fill="#bbb"/><circle cx="20" cy="5" r="4" fill="#bbb"/><circle cx="35" cy="5" r="4" fill="#bbb"/></svg></span>
    <span>English <svg width="8" height="6" viewBox="0 0 8 6"><path d="M0 0h8L4 6z" fill="#999"/></svg></span>
  </div>
  <nav class="main-nav">
    <a class="active" href="#">HOME</a>
    <a href="#">ABOUT US</a>
    <a href="#">THERAPISTS BIO</a>
    <a href="#">CONTACT US</a>
  </nav>
</header>

<section class="hero">
  <div class="hero-photo" role="img" aria-label="Photo of a therapist taking notes on a clipboard during a session with a client"></div>
  <p class="hero-quote">Our sorrows and wounds are<br><span class="accent">healed only when we touch</span><br>them with compassion<span class="author">- Orvelan</span></p>
  <div class="hero-arrows">
    <span><svg width="10" height="12" viewBox="0 0 10 12"><path d="M8 0L0 6l8 6z" fill="#fff"/></svg></span>
    <span><svg width="10" height="12" viewBox="0 0 10 12"><path d="M2 0l8 6-8 6z" fill="#fff"/></svg></span>
  </div>
</section>

<section class="intro">
  <div class="intro-copy">
    <h1>MARRIAGE AND FAMILY THERAPIST COOPERATIVE</h1>
    <p>Therapy can assist you in overcoming all of these challenges. Assist you in uncovering the difficulties and barriers that are keeping you from achieving your life’s ambitions, help discover ways to overcome them, and cope with the impact your behaviour has on your occupation, personal life and social life.</p>
    <p>Welcome to our practice, with over 20 years of combined experience in the clinical field you are sure to find the right fit for your needs. Each clinician has experience working with groups, adults, teens, children, families, and couples. We specialize in fostering healthy relationships between individuals, managing depression and anxiety, overcoming trauma, and developing occupational success. Feel free to explore information about each clinician and make an appointment with one of us today.</p>
    <a class="btn" href="#">READ MORE</a>
  </div>
  <aside class="contact-box">
    <header><div class="label">Contact Us</div><div class="phone">(951)555-0182</div></header>
    <form>
      <div class="field"></div>
      <div class="field"></div>
      <div class="field tall"></div>
      <a class="btn" href="#">SUBMIT</a>
    </form>
  </aside>
</section>

<section class="features">
  <article class="feature" style="left:100px">
    <div class="feature-photo" role="img" aria-label="Photo of a stressed woman sitting with her head in her hands" style="background:linear-gradient(135deg,#d9d4cc,#9c948a)"></div>
    <h2>Feeling stressed and overwhelmed?</h2>
    <p>Talking with a caring professional can ease the weight you carry and help you find calm, clarity and steady footing again.</p>
  </article>
  <article class="feature" style="left:440px">
    <div class="feature-photo" role="img" aria-label="Photo of a man working at a desk surrounded by books" style="background:linear-gradient(135deg,#c9ced3,#7d8690)"></div>
    <h2>Encountering barriers towards your goals?</h2>
    <p>Together we can uncover what is holding you back and build practical steps toward the life and work you truly want.</p>
  </article>
  <article class="feature" style="left:780px">
    <div class="feature-photo" role="img" aria-label="Photo of a counselor listening to a client on a sofa" style="background:linear-gradient(135deg,#e2ddd6,#a8a39c)"></div>
    <h2>Have the need to talk but unsure who to turn to?</h2>
    <p>Our team offers a warm, safe and confidential space where you can share openly and feel truly heard and supported.</p>
  </article>
</section>

<section class="testimonial">
  <div class="testimonial-photo" role="img" aria-label="Portrait photo of a client in a suit" style="background:linear-gradient(180deg,#d8d8d8,#6f7275)"></div>
  <span class="quote-mark" style="left:205px;top:6px">“</span>
  <blockquote>
    There are many moments in a family’s journey that feel heavy and hard to name. <span class="hl">Working with this cooperative gave us a place to slow down, listen to each other and rebuild trust.</span> Each session brought patient guidance and honest tools we still use at home. Our children are calmer, our marriage is stronger, and we finally feel like a team again. We are grateful for the care, the kindness and the steady support we received every single week.
  </blockquote>
  <span class="quote-mark" style="left:960px;top:112px">”</span>
  <cite>— Tomas Wrenfield</cite>
  <div class="dots"><span></span><span class="on"></span><span></span><span></span></div>
</section>

<footer class="site-footer">
  <div class="footer-col" style="left:100px">
    <h3>Information</h3>
    <ul><li>Home</li><li>About Us</li><li>Therapists Bio</li><li>Contact Us</li></ul>
  </div>
  <div class="footer-col" style="left:270px">
    <h3>Categories</h3>
    <ul><li>Individuals</li><li>Couples</li><li>Families</li><li>Children</li><li>Teens</li></ul>
  </div>
  <div class="footer-col" style="left:440px">
    <h3>Newsletter</h3>
    <p>Sign up for news, tips and updates from our team.</p>
    <div class="news-row"><div class="input"></div><div class="go">SUBSCRIBE</div></div>
  </div>
  <div class="footer-col contact-list" style="left:790px">
    <h3>Contact Us</h3>
    <ul>
      <li><svg width="10" height="12" viewBox="0 0 10 12"><path d="M5 0a4 4 0 0 0-4 4c0 3 4 8 4 8s4-5 4-8a4 4 0 0 0-4-4z" fill="#a9c23f"/></svg>Riverside, California</li>
      <li><svg width="10" height="10" viewBox="0 0 10 10"><path d="M2 0l2 2-1 2 3 3 2-1 2 2-2 2C4 10 0 6 0 2z" fill="#a9c23f"/></svg>(951)555-0182</li>
      <li><svg width="11" height="8" viewBox="0 0 11 8"><rect width="11" height="8" fill="#a9c23f"/><path d="M0 0l5.5 4L11 0" stroke="#1f1f1f" fill="none"/></svg>marisel582@postbox.example</li>
    </ul>
  </div>
  <div class="footer-col" style="left:1010px">
    <h3>Information</h3>
    <ul><li>Privacy</li><li>Terms</li><li>Sitemap</li></ul>
  </div>
  <div class="copyright">© 2024 Meadowgatecounselors.example</div>
</footer>

</body>
</html>
```